Stationery Design Project

Letterhead with logo and address
Envelopes with Logo and address

The target market is start-ups and
small to medium businesses primarly located in China, with less than 20
employees. Please have designers use Yellow and Blue colors and our logo
attached. Looking fr the same format as the business card attached.

Reason: Designer has been delayed working on web design

Target Market(s)

Start-ups and small to medium size businesses

Industry/Entity Type

Business

Font styles to use
Sans Serif

Requirements
Must have
• None
Nice to have
• None
Should not have
• N/A

```html
<!DOCTYPE html>
<html lang="en">
<head>
<meta charset="utf-8">
<title>Meridian Harbor Business Advisory – Letterhead</title>
<link href="https://fonts.googleapis.com/css2?family=Lato:wght@400;700&family=Noto+Sans+SC:wght@400&display=swap" rel="stylesheet">
<style>
  :root {
    --brand-blue: #0D4D80;
    --sidebar-blue: #0b4d80;
    --accent-yellow: #f5c32c;
    --paper: #ffffff;
    --text-light: #ffffff;
  }
  * { margin: 0; padding: 0; box-sizing: border-box; }
  html, body { width: 927px; height: 1200px; overflow: hidden; background: var(--paper); }
  .letterhead {
    position: relative;
    width: 927px;
    height: 1200px;
    font-family: "Lato", sans-serif;
    color: var(--brand-blue);
    background: var(--paper);
  }
  .sidebar {
    position: absolute;
    left: 0; top: 0;
    width: 195px; height: 1200px;
    background: var(--sidebar-blue);
  }
  .brand-mark {
    position: absolute;
    left: 0; top: 50px;
    width: 195px;
    display: flex;
    flex-direction: column;
    align-items: center;
    gap: 22px;
  }
  .brand-dot {
    width: 110px; height: 110px;
    border-radius: 50%;
    background: var(--accent-yellow);
  }
  .brand-name {
    font-weight: 700;
    font-size: 27px;
    letter-spacing: 7px;
    color: var(--text-light);
    padding-left: 7px;
  }
  .sidebar-web {
    position: absolute;
    left: 28px; top: 1140px;
    font-size: 12px;
    font-weight: 700;
    color: var(--text-light);
  }
  .company-header {
    position: absolute;
    left: 195px; top: 52px;
    width: 732px;
    text-align: center;
  }
  .company-name-zh {
    font-family: "Noto Sans SC", "Lato", sans-serif;
    font-size: 27px;
    letter-spacing: 1px;
    line-height: 40px;
  }
  .company-name-en {
    font-size: 27px;
    line-height: 30px;
    margin-top: 4px;
  }
  .body-copy {
    position: absolute;
    left: 224px; top: 220px;
    width: 670px;
  }
  .body-copy p { font-size: 14.5px; line-height: 30.5px; white-space: nowrap; }
  .body-copy .size-11 { font-size: 16.5px; }
  .body-copy .size-12 { font-size: 17.5px; }
  .body-end {
    position: absolute;
    right: 38px; top: 1083px;
    font-size: 14.5px;
  }
  .footer-contact {
    position: absolute;
    left: 195px; top: 1139px;
    width: 732px;
    text-align: center;
    font-size: 12px;
    font-weight: 700;
    line-height: 15.5px;
    letter-spacing: 0.3px;
  }
</style>
</head>
<body>
<main class="letterhead">
  <aside class="sidebar">
    <div class="brand-mark">
      <div class="brand-dot"></div>
      <div class="brand-name">MHBA</div>
    </div>
    <div class="sidebar-web">www.meridianharbor.cn</div>
  </aside>

  <header class="company-header">
    <h1 class="company-name-zh" style="font-weight:400">明港商务咨询（上海）有限公司</h1>
    <p class="company-name-en">Meridian Harbor Business Advisory<br>(Shanghai) Co., Ltd.</p>
  </header>

  <section class="body-copy">
    <p>THIS IS THE BODY START</p>
    <p>Typeface displayed here is Lato Regular 10 pt; hex color #0D4D80; CMYK 85, 50, 0, 40.</p>
    <p>Maximum number of characters in this row is 80, so the typeface size may be 11, even 12:</p>
    <p class="size-11">11 lorem ipsum lorem ipsum lorem ipsum lorem ipsum lorem ipsum</p>
    <p class="size-12">12 lorem ipsum lorem ipsum lorem ipsum lorem ipsum lorem ipsum</p>
  </section>

  <p class="body-end">THIS IS THE BODY END</p>

  <footer class="footer-contact">
    <p>Meridian Harbor Business Advisory (Shanghai) Co., Ltd.</p>
    <p>Lianhua Road 88, suite 210-212, Minhang Dist., Shanghai</p>
    <p>Phone: +86-021-55501234, Fax: +86-021-55501235</p>
  </footer>
</main>
</body>
</html>
```